Business Card Design, Harborline Growth Studio
Business Card Design for an Internet Marketing Company
Designers- please make sure your designs include the Social Media buttons for Friendloom, Quillet and ViewCrate. Also need the Vantiro Linkway logo.
RK/TWS Team
Designers- Please add a View Crate icon as I also plan on having a View Crate channel and I'd like to incorporate that on the card along with the other social media buttons. Thank you.
Designers: One thing I need added on the back of the card is something that says "Authorized Agent of Vantiro Linkway". You can visit www.vantirolinkway.example and see their logo. We probably will want to incorporate the Vantiro Linkway logo but if it's colors conflict, we may need to change the logo to a monochrome version of just use text. I am looking for ideas on how to include it, but it should have only a minimal impact on the look of the back side of the business card.
Designers- The AI file uploaded has the logo without a background and with a background. please feel free to use the logo with any background you feel will help you come up with the best design or without a background, your choice. Please don't let the background shown influence your decision. We are totally open to creative ideas. Thanks and good luck!!!

```html
<!DOCTYPE html>
<html lang="en">
<head>
<meta charset="utf-8">
<title>Harborline Growth Studio – Business Cards</title>
<link rel="stylesheet" href="https://fonts.googleapis.com/css2?family=Open+Sans:wght@400;600;700&display=swap">
<style>
  :root {
    --page-bg: #e4e4e2;
    --navy: #1f2a6b;
    --navy-deep: #141b4a;
    --navy-light: #3a4aa0;
    --red: #d3202c;
    --ink: #4a4d57;
    --card-white: #ffffff;
    --white-soft: rgba(255, 255, 255, 0.78);
    --shadow: rgba(20, 24, 50, 0.25);
  }
  * { box-sizing: border-box; margin: 0; padding: 0; }
  html, body {
    width: 1200px;
    height: 901px;
    overflow: hidden;
    background: var(--page-bg);
    font-family: "Open Sans", Arial, sans-serif;
  }
  .sheet {
    position: relative;
    width: 1200px;
    height: 901px;
    display: flex;
    align-items: center;
    justify-content: center;
    gap: 40px;
  }
  .card {
    position: relative;
    width: 540px;
    height: 309px;
    border-radius: 26px;
    overflow: hidden;
    box-shadow: 0 10px 28px var(--shadow);
  }

  /* Back side */
  .card-back {
    display: flex;
    align-items: center;
    justify-content: center;
  }
  .card-back .backdrop {
    position: absolute;
    inset: 0;
    background: radial-gradient(ellipse at 50% 40%, var(--navy-light) 0%, var(--navy) 45%, var(--navy-deep) 100%);
  }
  .brand {
    position: relative;
    display: flex;
    align-items: center;
    gap: 12px;
    font-weight: 700;
    text-transform: uppercase;
    letter-spacing: 0.02em;
    white-space: nowrap;
  }
  .brand-mark {
    width: 22px;
    height: 22px;
    background: var(--red);
    flex: none;
  }
  .card-back .brand {
    color: var(--card-white);
    font-size: 26px;
  }
  .agent-line {
    position: absolute;
    left: 0;
    right: 0;
    bottom: 26px;
    text-align: center;
    color: var(--white-soft);
    font-size: 11px;
    letter-spacing: 0.06em;
  }

  /* Front side */
  .card-front {
    background: var(--card-white);
    padding: 38px 44px;
  }
  .card-front .brand {
    color: var(--navy);
    font-size: 21px;
    margin-bottom: 40px;
  }
  .card-front .brand-mark {
    width: 18px;
    height: 18px;
  }
  .person-name {
    color: var(--red);
    font-size: 17px;
    font-weight: 600;
    line-height: 1.2;
  }
  .person-title {
    color: var(--ink);
    font-size: 12.5px;
    margin-bottom: 10px;
  }
  .details {
    list-style: none;
    color: var(--ink);
    font-size: 12.5px;
    line-height: 1.55;
  }
  .details li {
    display: flex;
    align-items: center;
    gap: 7px;
    white-space: nowrap;
  }
  .details svg {
    width: 11px;
    height: 11px;
    flex: none;
  }
  .social-list {
    position: absolute;
    right: 40px;
    bottom: 38px;
    list-style: none;
    color: var(--navy);
    font-size: 12px;
    line-height: 1.7;
  }
  .social-list li {
    display: flex;
    align-items: center;
    gap: 7px;
  }
  .social-dot {
    width: 10px;
    height: 10px;
    border-radius: 50%;
    background: var(--navy);
    flex: none;
  }
</style>
</head>
<body>
<main class="sheet">
  <section class="card card-back">
    <div class="backdrop" role="img" aria-label="Deep navy background with fine halftone dot texture"></div>
    <div class="brand"><span class="brand-mark"></span>Harborline Growth Studio</div>
    <p class="agent-line">Authorized Agent of Vantiro Linkway</p>
  </section>

  <section class="card card-front">
    <div class="brand"><span class="brand-mark"></span>Harborline Growth Studio</div>
    <p class="person-name">Dale Ransome</p>
    <p class="person-title">Chief Executive Officer</p>
    <ul class="details">
      <li>P.O. Box 418</li>
      <li>Cedar Bend, NJ 07911</li>
      <li>
        <svg viewBox="0 0 12 12" aria-hidden="true"><rect width="12" height="12" rx="2" fill="#d3202c"/><path d="M3.5 2.8c.5-.3.9-.1 1.1.3l.5 1c.2.4 0 .7-.3.9l-.3.2c.3.8.9 1.4 1.7 1.7l.2-.3c.2-.3.5-.5.9-.3l1 .5c.4.2.6.6.3 1.1-.5.8-1.3 1-2.1.7C4.6 8 3.6 7 3.1 5.2c-.3-.9 0-1.8.4-2.4z" fill="#fff"/></svg>
        555 014 2286
      </li>
      <li>
        <svg viewBox="0 0 12 12" aria-hidden="true"><rect width="12" height="12" rx="2" fill="#d3202c"/><rect x="2.5" y="3.5" width="7" height="5" fill="none" stroke="#fff" stroke-width="1"/><path d="M2.5 3.5 6 6.3 9.5 3.5" fill="none" stroke="#fff" stroke-width="1"/></svg>
        dale.ransome@harborlinegrowthstudio.net
      </li>
      <li>www.harborlinegrowthstudio.net</li>
    </ul>
    <ul class="social-list">
      <li><span class="social-dot"></span>Friendloom</li>
      <li><span class="social-dot"></span>Quillet</li>
      <li><span class="social-dot"></span>ViewCrate</li>
    </ul>
  </section>
</main>
</body>
</html>
```